Looking for Landingpage / Website Designer

We are looking for a Web Designer / Developer for our upcoming Start Up Websites. The first project will be a simple responsive business website with a CTA- Button and an optional Newsletter Opt-In. We do aim for a modern online business approach, since we are a young company.

It is necessary to understand, that we need a conversion orientated design, not a wordpress blog with widgets and galleries.

We are currently discussing how it is going to happen and what preferences we need to focus on.

What we know is, that it should be more of a landing page with an option of adding 2 or 3 Navigation points.

We even thought about using services like pagemarlo.com or formvista.com to have an easier approach for future customizations and A/B testing.

We'd love to see how you fit the design/colors to the upcoming logo
(which is not the final version yet )

hope you can do something about that.

For the Structure.

1. Bracket

Slogan plus a preview text of what we are offering. On the right side a video placeholder plus CTA button.

2. Bracket

Illustrating 3 Benefits. On the right side - Opt in for Contact/Newsletter and CTA Button

3. Bracket

Picture with text just like you have it with the testimonial

You can orientate yourself towards to that landing page example as well:

http://cdn2.quentarix.net/hub/53/file-581676469-png/Blog-Related_Images/pagemarlo_landing_page.png?t=1416543075530

If our collaboration is going well, we would like to stay in touch for further projects.

Reason: There are 3 Design we do really like but, don't fit exactly our needs. 5 Days max.

Reason: For final adjustments.

I just uploaded the final logo :) Thank you for your commitment so far!

Target Market(s)

Our targeted audience could be almost everybody, who looks for an average paid side job (students, unemployed, house wives and whatever you can imagine). Maybe this is enough information for you to get a mere perception of what this is all about.

Industry/Entity Type

Business

Coding

Coded - Design and coding required

Font styles to use
Serif
Sans Serif

Colors
acd037
5c5c5c
33a6d7

Requirements
Must have
• Registration Opt-In
Responsive on any Device
Customizable
A benefits navigation just like in that example I've uploaded.
Nice to have
• As fast as possible ;D

```html
<!DOCTYPE html>
<html lang="en">
<head>
<meta charset="utf-8">
<title>Worklyn.de – Landing Page</title>
<link href="https://fonts.googleapis.com/css2?family=Open+Sans:ital,wght@0,400;0,600;0,700;0,800;1,700;1,800&family=Questrial&display=swap" rel="stylesheet">
<style>
  :root{
    --green:#acd037;
    --green-deep:#5fb440;
    --blue:#33a6d7;
    --gray:#5c5c5c;
    --gray-dark:#4a4a4a;
    --gray-band:#515151;
    --stone:#8f8c84;
    --ink:#222;
    --white:#fff;
    --footer:#3d3d3d;
  }
  *{box-sizing:border-box;margin:0;padding:0}
  html,body{width:712px;height:1200px;overflow:hidden}
  body{position:relative;background:var(--white);font-family:"Open Sans",Arial,sans-serif;color:var(--ink)}
  .abs{position:absolute}

  /* header */
  .site-header{left:0;top:0;width:712px;height:43px;background:var(--white)}
  .brand{left:50px;top:6px;display:flex;align-items:center;gap:8px}
  .brand-dot{width:28px;height:28px;border-radius:50%;background:var(--green-deep)}
  .brand-name{font-weight:700;font-size:24px;color:var(--gray)}
  .partners{left:306px;top:14px;display:flex;align-items:center;gap:18px}
  .partners-lead{font-weight:700;font-style:italic;font-size:12px;color:var(--blue)}
  .partner{font-weight:700;font-size:10px;color:var(--ink)}

  /* benefits */
  .benefits{left:0;top:43px;width:712px;height:329px;background:var(--gray)}
  .card{top:39px;width:202px}
  .card-head{height:48px;font-family:"Questrial",sans-serif;font-size:30px;color:var(--white);text-align:center;line-height:50px}
  .card-head.green{background:var(--green-deep)}
  .card-head.blue{background:var(--blue)}
  .card-head.stone{background:var(--stone);color:var(--ink)}
  .card-photo{height:68px;background:linear-gradient(180deg,#d8d8d8,#8a8a8a)}
  .card-photo.dark{background:linear-gradient(180deg,#555,#1c1c1c)}
  .card-text{padding:12px 10px 0;font-size:9.5px;line-height:12px;color:var(--white)}
  .card-cta{display:block;text-align:right;padding:4px 14px 0 0;font-weight:800;font-style:italic;font-size:10.5px}
  .card-cta.green{color:var(--green-deep)}
  .card-cta.blue{color:var(--blue)}
  .card-cta.stone{color:#2a2a2a}

  .benefit-nav{left:46px;top:249px;width:622px;height:62px;background:var(--gray-band)}
  .nav-btn{top:16px;width:183px;height:40px;background:#666;box-shadow:0 2px 4px rgba(0,0,0,.45);display:flex;align-items:center;gap:12px;padding-left:12px;font-family:"Questrial",sans-serif;font-size:20px;color:var(--white)}
  .nav-btn svg{flex:none}

  /* newsletter */
  .featured{left:0;top:372px;width:712px;height:312px;background:var(--blue)}
  .featured-title{left:74px;top:44px;font-weight:700;font-size:21px;color:var(--white);letter-spacing:.3px}
  .featured-copy{left:72px;top:78px;width:310px;font-weight:600;font-size:10.5px;line-height:15.5px;color:var(--white)}
  .featured-copy p+p{margin-top:15px}
  .featured-cta{display:block;text-align:right;font-weight:800;font-style:italic;margin-top:2px}
  .signup-shadow{left:430px;top:48px;width:246px;height:250px;background:var(--green-deep)}
  .signup{left:415px;top:37px;width:248px;height:250px;background:var(--gray);border:3px solid #3e3e3e;box-shadow:0 2px 6px rgba(0,0,0,.35)}
  .signup-icon{left:18px;top:22px}
  .signup-title{left:62px;top:33px;font-weight:700;font-size:14.5px;color:var(--green-deep)}
  .signup-sub{left:62px;top:52px;font-weight:600;font-size:10px;color:var(--green-deep)}
  .field{left:35px;width:175px;height:34px;background:#3f3f3f;border:2px solid #7a7a7a;border-radius:8px}
  .submit{left:38px;top:189px;width:170px;height:28px;background:#6b6b6b;color:var(--green-deep);font-weight:800;font-size:16px;letter-spacing:.5px;text-align:center;line-height:28px}

  /* pitch */
  .pitch{left:0;top:692px;width:712px;height:218px;background:var(--gray)}
  .pitch-title{left:60px;top:24px;width:320px;font-weight:700;font-size:17.5px;line-height:20px;color:var(--green-deep)}
  .pitch-btn{left:63px;top:118px;width:166px;height:42px;background:var(--blue);display:flex;align-items:center;gap:14px;padding-left:4px;font-weight:700;font-size:17.5px;color:var(--white)}
  .video{left:400px;top:21px;width:275px;height:178px;background:radial-gradient(ellipse at 50% 45%,#3a3a3a,#0c0c0c 70%);border:1px solid #222}
  .video-play{left:122px;top:66px;width:30px;height:30px;border-radius:50%;background:#5a5a5a;border:2px solid #888}
  .video-bar{left:0;bottom:0;width:100%;height:14px;background:#1a1a1a;border-top:1px solid #444}

  /* testimonials */
  .voices{left:0;top:910px;width:712px;height:270px;background:var(--white)}
  .voices-art{left:48px;top:38px;width:162px;height:174px;background:radial-gradient(circle at 45% 35%,#e2e2e2,#cfcfcf 60%,#ececec)}
  .voices-title{left:60px;top:86px;width:300px;text-align:center;font-weight:700;font-size:25px;line-height:29px;color:var(--blue)}
  .quote{left:360px;width:300px;height:60px}
  .avatar{left:0;top:0;width:58px;height:58px;border-radius:50%;background:linear-gradient(180deg,#e6c9a8,#8a6d52);border:2px solid #ddd}
  .quote-text{left:78px;top:6px;width:210px;font-weight:700;font-style:italic;font-size:8px;line-height:11px;color:var(--ink)}
  .quote-name{left:78px;top:50px;width:210px;text-align:right;font-weight:700;font-style:italic;font-size:8px;color:var(--blue)}

  .site-footer{left:0;top:1180px;width:712px;height:20px;background:var(--footer);color:#ddd;font-size:8px;text-align:center;line-height:20px}
</style>
</head>
<body>

<header class="abs site-header">
  <div class="abs brand"><span class="brand-dot"></span><span class="brand-name">Worklyn.de</span></div>
  <div class="abs partners">
    <span class="partners-lead">We are Proud to advertise for.....</span>
    <span class="partner">Halvern</span><span class="partner">Orvo</span><span class="partner">Pixelon</span><span class="partner">Marevia</span>
  </div>
</header>

<section class="abs benefits">
  <article class="abs card" style="left:46px">
    <h2 class="card-head green">HEADING1</h2>
    <div class="card-photo" role="img" aria-label="Silhouettes of a team in front of a world map"></div>
    <p class="card-text">This is dummy text and real content will be here very soon. This is dummy text for now and actual content will ...</p>
    <a class="card-cta green">GET STARTED!</a>
  </article>
  <article class="abs card" style="left:253px">
    <h2 class="card-head blue">HEADING 2</h2>
    <div class="card-photo" role="img" aria-label="Smiling business team photo"></div>
    <p class="card-text">This is dummy text and real content will be here very soon. This is dummy text for now and actual content will ...</p>
    <a class="card-cta blue">GET STARTED!</a>
  </article>
  <article class="abs card" style="left:460px">
    <h2 class="card-head stone">HEADING 3</h2>
    <div class="card-photo dark" role="img" aria-label="Hand touching floating digital screens"></div>
    <p class="card-text">This is dummy text and real content will be here very soon. This is dummy text for now and actual content will ...</p>
    <a class="card-cta stone">GET STARTED!</a>
  </article>

  <nav class="abs benefit-nav">
    <div class="abs nav-btn" style="left:15px">
      <svg width="24" height="18" viewBox="0 0 24 18"><circle cx="6" cy="5" r="3.5" fill="#5fb440"/><circle cx="17" cy="5" r="3.5" fill="#5fb440"/><rect x="1" y="10" width="10" height="8" fill="#5fb440"/><rect x="12" y="10" width="10" height="8" fill="#5fb440"/></svg>
      WHO WE ARE
    </div>
    <div class="abs nav-btn" style="left:219px">
      <svg width="20" height="20" viewBox="0 0 20 20"><rect x="1" y="9" width="4" height="10" fill="#5fb440"/><path d="M6 9 L10 2 Q12 1 12 4 L11 8 H18 Q19 9 18 11 L16 18 H6 Z" fill="#5fb440"/></svg>
      WHY US
    </div>
    <div class="abs nav-btn" style="left:423px">
      <svg width="18" height="22" viewBox="0 0 18 22"><rect x="5" y="1" width="4" height="11" rx="2" fill="#5fb440"/><path d="M3 10 H15 V18 Q15 21 12 21 H6 Q3 21 3 18 Z" fill="#5fb440"/></svg>
      GET STARTED
    </div>
  </nav>
</section>

<section class="abs featured">
  <h2 class="abs featured-title">THIS IS FEATURED HEADING</h2>
  <div class="abs featured-copy">
    <p>This is dummy text and real content will be here very soon. This is dummy text for now and actual content will be here very soon. This is dummy text and real content will be here very soon. This is dummy text for now and actual content will be here very soon.</p>
    <p>This is dummy text and real content will be here very soon. This is dummy text for now and actual content will ...</p>
    <a class="featured-cta">GET STARTED!</a>
  </div>
  <div class="abs signup-shadow"></div>
  <form class="abs signup">
    <svg class="abs signup-icon" width="44" height="62" viewBox="0 0 44 62"><rect x="2" y="2" width="26" height="56" rx="4" fill="none" stroke="#777" stroke-width="3"/><rect x="14" y="26" width="28" height="18" fill="#5c5c5c" stroke="#777" stroke-width="2.5"/><path d="M14 26 L28 37 L42 26" fill="none" stroke="#777" stroke-width="2.5"/></svg>
    <div class="abs signup-title">GET FREE NEWSLETTER</div>
    <div class="abs signup-sub">in your inbox for Latest Offers!!!</div>
    <div class="abs field" style="top:96px"></div>
    <div class="abs field" style="top:140px"></div>
    <div class="abs submit">SUBMIT</div>
  </form>
</section>

<section class="abs pitch">
  <h2 class="abs pitch-title">LOOKING FORWARD TO AN EFFECTIVE SOLUTION TO TOURN YOUR VISITORS TO YOU CUSTOMER ?</h2>
  <a class="abs pitch-btn">
    <svg width="26" height="20" viewBox="0 0 26 20"><path d="M1 10 H23 M14 2 L23 10 L14 18" fill="none" stroke="#4a4a4a" stroke-width="3"/></svg>
    GET STARTED
  </a>
  <div class="abs video">
    <div class="abs video-play"><svg width="26" height="26" viewBox="0 0 26 26"><path d="M10 8 L18 13 L10 18 Z" fill="#222"/></svg></div>
    <div class="abs video-bar"></div>
  </div>
</section>

<section class="abs voices">
  <div class="abs voices-art" role="img" aria-label="Faint illustration of a support agent with a headset"></div>
  <h2 class="abs voices-title">SEE WHAT<br>OUR CUSTOMERS<br>ARE SAYING ABOUT<br>OUR SERVICE</h2>

  <div class="abs quote" style="top:27px">
    <div class="abs avatar" role="img" aria-label="Customer portrait"></div>
    <p class="abs quote-text">We are Amazed with their service. this is just dummy text for now and real text will be here soon. This is just dummy text for now.</p>
    <p class="abs quote-name">- Nora Quellet - Member of B.R.I.G.H.T</p>
  </div>
  <div class="abs quote" style="top:105px">
    <div class="abs avatar" role="img" aria-label="Customer portrait"></div>
    <p class="abs quote-text">We are Amazed with their service. this is just dummy text for now and real text will be here soon. This is just dummy text for now.</p>
    <p class="abs quote-name">- Tobias Renfeld - Canopy corporation</p>
  </div>
  <div class="abs quote" style="top:185px">
    <div class="abs avatar" role="img" aria-label="Customer portrait"></div>
    <p class="abs quote-text">We are Amazed with their service. this is just dummy text for now and real text will be here soon. This is just dummy text for now.</p>
    <p class="abs quote-name">- Marc Dulwich - Trivane</p>
  </div>
</section>

<footer class="abs site-footer">Copyright 2014 - www.yourfirmsite.com - All rights reserved.</footer>

</body>
</html>
```